Q-Rolls Business Card

We are a modern retail clothing store. Established in 1994. I need a presentable card that will amaze vendors when given to them.

Front: Logo in middle
Info Side:

Name: Tomas Velder
Cell: 630-812-4463
Work: 630-917-3384 EXT. 417
Email: Tomas@q-rolls-example.com
Website: www.Q-rolls-example.com

Industry/Entity Type

Business

```html
<!DOCTYPE html>
<html lang="en">
<head>
<meta charset="utf-8">
<title>Q-Rolls Business Card</title>
<link href="https://fonts.googleapis.com/css2?family=Source+Sans+3:wght@400;600&display=swap" rel="stylesheet">
<style>
  :root {
    --backdrop: #e4e2e0;
    --card: #111111;
    --ink: #ffffff;
    --ink-soft: #d6d6d6;
    --ink-muted: #9a9a9a;
    --rule: #6d6d6d;
  }
  * { margin: 0; padding: 0; box-sizing: border-box; }
  html, body { width: 1200px; height: 814px; overflow: hidden; }
  body {
    background: var(--backdrop);
    font-family: "Source Sans 3", "Myriad Pro", Arial, sans-serif;
    display: flex;
    align-items: center;
    justify-content: center;
    gap: 40px;
  }
  .card {
    width: 540px;
    height: 309px;
    background: var(--card);
    color: var(--ink);
    position: relative;
    box-shadow: 0 10px 28px rgba(0,0,0,0.25);
  }
  .brand-name {
    font-weight: 600;
    color: var(--ink);
    letter-spacing: 1px;
    line-height: 1;
    white-space: nowrap;
  }
  /* Info side */
  .info-card .brand-name {
    position: absolute;
    left: 52px;
    top: 150px;
    font-size: 46px;
  }
  .info-card .divider {
    position: absolute;
    left: 272px;
    top: 72px;
    width: 1px;
    height: 170px;
    background: linear-gradient(to bottom, transparent, var(--rule) 20%, var(--rule) 80%, transparent);
  }
  .contact {
    position: absolute;
    left: 296px;
    top: 78px;
  }
  .contact-name {
    font-size: 17px;
    font-weight: 600;
    color: var(--ink-muted);
  }
  .contact-role {
    font-size: 13px;
    color: var(--ink-soft);
    margin-bottom: 14px;
  }
  .contact-list { list-style: none; }
  .contact-list li {
    display: flex;
    align-items: center;
    gap: 10px;
    font-size: 13.5px;
    color: var(--ink-soft);
    line-height: 22px;
  }
  .contact-list svg { width: 13px; height: 13px; flex: none; }
  /* Logo side */
  .logo-card .brand-name {
    position: absolute;
    left: 0; right: 0;
    top: 104px;
    text-align: center;
    font-size: 64px;
  }
  .site-line {
    position: absolute;
    left: 0; right: 0;
    top: 210px;
    display: flex;
    align-items: center;
    justify-content: center;
    gap: 10px;
    font-size: 11px;
    letter-spacing: 3px;
    color: var(--ink-soft);
  }
  .site-line .stroke {
    width: 60px;
    height: 1px;
    background: var(--ink-soft);
  }
</style>
</head>
<body>
  <section class="card info-card">
    <div class="brand-name">Q-Rolls</div>
    <div class="divider"></div>
    <div class="contact">
      <div class="contact-name">Tomas Velder</div>
      <div class="contact-role">CEO/Founder</div>
      <ul class="contact-list">
        <li>
          <svg viewBox="0 0 14 14" aria-hidden="true"><rect x="3.5" y="1" width="7" height="12" rx="1.2" fill="none" stroke="#d6d6d6" stroke-width="1.3"/><circle cx="7" cy="11" r="0.8" fill="#d6d6d6"/></svg>
          630-812-4463
        </li>
        <li>
          <svg viewBox="0 0 14 14" aria-hidden="true"><path d="M3 1.5l2.2 2.6-1.2 1.5c.8 1.8 2.2 3.2 4 4l1.5-1.2 2.6 2.2-1.3 1.9C5.8 12.4 1.6 8.2 1.1 2.8z" fill="#d6d6d6"/></svg>
          630-917-3384 EXT. 417
        </li>
        <li>
          <svg viewBox="0 0 14 14" aria-hidden="true"><rect x="1" y="3" width="12" height="8.5" fill="#d6d6d6"/><path d="M1 3l6 5 6-5" fill="none" stroke="#111" stroke-width="1.1"/></svg>
          Tomas@q-rolls-example.com
        </li>
        <li>
          <svg viewBox="0 0 14 14" aria-hidden="true"><circle cx="7" cy="7" r="5.8" fill="none" stroke="#d6d6d6" stroke-width="1.3"/><ellipse cx="7" cy="7" rx="2.4" ry="5.8" fill="none" stroke="#d6d6d6" stroke-width="1"/><line x1="1.2" y1="7" x2="12.8" y2="7" stroke="#d6d6d6" stroke-width="1"/></svg>
          www.Q-rolls-example.com
        </li>
      </ul>
    </div>
  </section>

  <section class="card logo-card">
    <div class="brand-name">Q-Rolls</div>
    <div class="site-line">
      <span class="stroke"></span>
      <span>www.Q-rolls-example.com</span>
      <span class="stroke"></span>
    </div>
  </section>
</body>
</html>
```